Halvorsen Spa

We are a large Miami Beach spa and salon. I am still building our website but you can use it as a resource to gain a better understanding of who we are ....www.spaquillowave.com.

We offer a comprehensive list of services in hair, nails, massage, skin care, tanning, spray tanning and waxing and we offer high quality products for skin care, tanning and hair. We are open 7 days.

We would like to see a clean and simple menu that looks a lot like the one from "The Spa at Brightmere." In particular, we have a copy of a menu from their West Hollywood, CA location that is just beautiful. In the uploaded content you will see a sampling of that menu. We would like to see greys, blacks, silvers, whites and warm colors like reds and oranges. We specifically attempt to remain gender neutral so that we don't attract only girls (with pink colors and flowers etc). The final design should convey a simple, clean, friendly environment and the final product should be sized such that it is 1.) portable and 2.) inexpensive to print. We will be running thousands of these at a time so cost of printing is a consideration.

The booklet consists of two parts: one part is the standard menu with descriptions of services and products and photos etc (think of this as the sales piece that convinces a potential customer to visit) and will be stapled together like you would expect a small menu to be and should resemble the Brightmere menu. The prices should not be included in this part of the booklet that will be printed and stapled. The other part is a single insert and is removable and replaceable. I want this removable insert placed in the last page of the book in a folder pocket or something else that you can think of so that when it's time to change prices here that I am not throwing away all of the booklets....I am only replacing the inserts at the end of the menu booklet. Please design this single page insert so that should a customer remove it from the booklet and keep it, that it stands alone with our name, logo, website and phone number. This page can and probably will have to be 2 sided.

At the back of the booklet, I also want the polices to be printed in one page (think fine print in any sort of business dealing.)

With regard to the look and feel slider of economical v upmarket...we definitely want to convey we deliver upmarket services at reasonable prices. Think, world class services and products at reasonable, everyday prices.

With regard to the uploaded files:
I uploaded both EPS and TIF formats. The colors in those files are not the palette we want at all. The colors we want use for the circular logo must match the standard colors as depicted in the uploaded file "Halvorsentanrooms"

Target Market(s)

The target market is the average 20-35 year old in Miami Beach that cares about their appearance. The range of clientele is quite diverse.

Industry/Entity Type

Environment

Requirements
Must have
• It must have elegant and simple photographs that relate to the services being offered. We are selling a service set and an environment...so this menu should be reflect that goal. The logo should be repeated often throughout the book but in subtle ways.

Stock photos are fine as long as they don't seem obviously stock.

Should not have
• Nothing buddha like. Nothing themed. It should be all inclusive and not seek to identify with any particular group or gender.

Nothing that fits the stereotype of "Miami Beach." We want to represent ourselves in the same category as the best spas in the world because we moving everything we do in that direction. Think class!

```html
<!DOCTYPE html>
<html lang="en">
<head>
<meta charset="utf-8">
<title>Nails Menu Spread</title>
<link href="https://fonts.googleapis.com/css2?family=Cardo:ital,wght@0,400;0,700;1,400&family=Tinos:ital,wght@0,400;0,700;1,400&display=swap" rel="stylesheet">
<style>
  :root {
    --panel-bg: #f3dfcb;
    --heading-red: #b45a3b;
    --item-ink: #6a2a1c;
    --body-ink: #7d706a;
    --title-ink: #6b5a52;
    --dot-line: #b98a76;
    --caption-ink: #f4f1ee;
  }
  * { box-sizing: border-box; margin: 0; padding: 0; }
  html, body { width: 1200px; height: 388px; overflow: hidden; background: #fff; }
  .spread { position: relative; width: 1200px; height: 388px; display: flex; }

  .menu-panel {
    position: relative; width: 448px; height: 388px; background: var(--panel-bg);
    font-family: "Cardo", serif; overflow: hidden;
  }
  .menu-title {
    position: absolute; left: 8px; top: 6px;
    font-family: "Cardo", serif; font-weight: 400; font-size: 21px; line-height: 28px;
    color: var(--title-ink); letter-spacing: 0.5px;
  }
  .price-label {
    position: absolute; top: 18px; font-family: "Tinos", serif; font-style: italic;
    font-size: 10px; line-height: 14px; color: var(--title-ink);
  }
  .price-label.residents { left: 300px; }
  .price-label.guests { left: 370px; }

  .group-heading {
    position: absolute; left: 8px; width: 428px;
    font-family: "Tinos", serif; font-weight: 400; font-size: 10px; line-height: 12px;
    color: var(--heading-red); text-transform: uppercase; letter-spacing: 0.2px;
    border-bottom: 1px dotted var(--dot-line); padding-bottom: 1px;
  }
  .group-desc {
    position: absolute; left: 8px; width: 428px;
    font-family: "Cardo", serif; font-size: 8.3px; line-height: 13.6px;
    color: var(--body-ink); letter-spacing: 0.4px;
  }
  .group-desc .line {
    display: block; white-space: nowrap;
    text-align: justify; text-align-last: justify;
  }
  .group-desc .line.last { text-align: left; text-align-last: left; }
  .price-list { position: absolute; left: 8px; width: 428px; list-style: none; }
  .price-row {
    position: relative; font-family: "Tinos", serif; font-size: 10px;
    line-height: 14px; color: var(--item-ink); white-space: nowrap;
  }
  .price-row .res, .price-row .hotel { position: absolute; top: 0; }
  .price-row .res { left: 292px; }
  .price-row .hotel { left: 364px; }

  .photo-hand {
    width: 152px; height: 388px;
    background: linear-gradient(90deg, #f2efec 0%, #e2d7cf 35%, #cdb9ab 70%, #b49c8d 100%);
  }
  .photo-tanning {
    position: relative; width: 600px; height: 388px;
    background:
      radial-gradient(ellipse 220px 60px at 560px 40px, rgba(220,245,250,.9), transparent 70%),
      radial-gradient(ellipse 250px 90px at 470px 330px, rgba(150,225,235,.55), transparent 70%),
      linear-gradient(90deg, #6e2a20 0%, #9a4a38 20%, #8b5a4a 38%, #4a3a36 60%, #232325 80%, #1a1c1f 100%);
  }
  .caption {
    position: absolute; left: 34px; top: 340px;
    font-family: "Cardo", serif; font-size: 13.6px; line-height: 20px;
    color: var(--caption-ink); letter-spacing: 0.5px; white-space: nowrap;
  }
  .caption .line-two { display: block; padding-left: 91px; }
</style>
</head>
<body>
<div class="spread">
  <section class="menu-panel">
    <h1 class="menu-title">{ Nails }</h1>
    <span class="price-label residents">Residents</span>
    <span class="price-label guests">Hotel Guests</span>

    <h2 class="group-heading" style="top:44px">Nail Bar Polishing</h2>
    <p class="group-desc" style="top:59px">
      <span class="line">Especially designed for those in a rush! We'll remove existing lacquer, apply a fresh coat</span>
      <span class="line last">of your favorite lacquer and you'll finish with a quick dry to get you on your way.</span>
    </p>
    <ul class="price-list" style="top:88px">
      <li class="price-row">Hand Polish Change<span class="res">$10.00</span><span class="hotel">$12.00</span></li>
      <li class="price-row">Foot Polish Change<span class="res">$12.00</span><span class="hotel">$13.00</span></li>
      <li class="price-row">Polish Combination<span class="res">$19.00</span><span class="hotel">$25.00</span></li>
    </ul>

    <h2 class="group-heading" style="top:140px">The Express</h2>
    <p class="group-desc" style="top:155px">
      <span class="line">If you are in a mad rush but absolutely need to pay a few minutes' attention to your hands</span>
      <span class="line">and feet, we have the perfect option. We include just the essentials- removal of existing</span>
      <span class="line">nail lacquer, a quick soak, cuticle grooming, nail shaping and the application of your</span>
      <span class="line last">favorite lacquer. This option will get you in and out in no time!</span>
    </p>
    <ul class="price-list" style="top:211px">
      <li class="price-row">The 15-Minute Express Manicure<span class="res">$15.00</span><span class="hotel">$18.00</span></li>
      <li class="price-row">The 30-Minute Express Pedicure<span class="res">$25.00</span><span class="hotel">$30.00</span></li>
      <li class="price-row">The 45-Minute Express Combination<span class="res">$39.00</span><span class="hotel">$45.00</span></li>
    </ul>

    <h2 class="group-heading" style="top:256px">The Classic</h2>
    <p class="group-desc" style="top:271px">
      <span class="line">Our Classic option is just what your nails need on a regular basis. We start with a purify-</span>
      <span class="line">ing and thorough soak to soften your nails and cuticles. We then follow with an aromatic,</span>
      <span class="line">exfoliating massage of the hands and the feet, designed to smooth and soften your hands</span>
      <span class="line">and feet. We remove your existing laquer, groom and oil your cuticles, shape and buff</span>
      <span class="line last">your nails and finish with the application of your favorite nail lacquer.</span>
    </p>
    <ul class="price-list" style="top:340px">
      <li class="price-row">The Classic Manicure<span class="res">$19.00</span><span class="hotel">$23.00</span></li>
      <li class="price-row">The Classic Pedicure<span class="res">$34.00</span><span class="hotel">$40.00</span></li>
      <li class="price-row">The Classic Combination<span class="res">$49.00</span><span class="hotel">$60.00</span></li>
    </ul>
  </section>

  <div class="photo-hand" role="img" aria-label="Close-up photograph of a hand with French-manicured nails"></div>

  <div class="photo-tanning" role="img" aria-label="Photograph of a glowing tanning bed in a dim room beside a potted bamboo plant and shoji screens">
    <p class="caption">{ I wanted this feeling<span class="line-two">to last forever ... }</span></p>
  </div>
</div>
</body>
</html>
```